Premium modern eliquids labels 84.5 x 80 mm

I am looking for modern graphics for the labels of a new eliquid line that will have 4 different types of eliquids. It will have a tobacco one (brown colours maybe), a fruity one (bright colours maybe), a minty one (green colours maybe) and a creamy one (beige colours maybe).
I will need one of them to see how the design is, that design will have to be adapted to the other 3 colours of the label.
The brand logo is attached. I also attached a sample of what is mandatory to write on the label, you can change size, place and font of what is written, the only thing that cannot be reduced is the yellow parts. I attach the bottle that we will use.The size of the label is 84.5 x 80 mm (base x height).

Target Market(s)

vapers

Requirements
Must have
• My project must have one of the labels.

```html
<!DOCTYPE html>
<html lang="it">
<head>
<meta charset="utf-8">
<title>Tobacco – Premium E-Liquid Label</title>
<link href="https://fonts.googleapis.com/css2?family=Archivo+Narrow:wght@400;700&family=Oswald:wght@500&family=Montserrat:wght@400&display=swap" rel="stylesheet">
<style>
  :root{
    --page:#dcdcdc;
    --label-dark:#191818;
    --label-mid:#2e2d2c;
    --ink:#ffffff;
    --tobacco:#8c5a33;
    --tobacco-light:#c9a98a;
    --tobacco-pale:#dcc3a8;
    --brand:#a88f7e;
    --badge:#f5c518;
    --badge-ink:#000000;
  }
  *{margin:0;padding:0;box-sizing:border-box}
  html,body{width:1200px;height:865px;overflow:hidden;background:var(--page)}
  .label{
    position:absolute;left:163px;top:20px;width:874px;height:826px;
    background:radial-gradient(ellipse at 50% 45%,var(--label-mid) 0%,var(--label-dark) 75%);
    color:var(--ink);font-family:"Archivo Narrow",Arial,sans-serif;font-weight:700;
  }
  .label > *{position:absolute}
  .ingredients{left:26px;top:32px;font-size:22px;line-height:26px;z-index:2}
  .instructions{left:696px;top:32px;width:160px;font-size:22px;line-height:25px;z-index:2}
  .ring{left:0;top:0;width:874px;height:826px}
  .flavour-swirl{left:215px;top:92px;width:425px;height:140px;border-radius:80px 36px 80px 36px;
    background:linear-gradient(90deg,var(--tobacco) 0%,var(--tobacco-light) 55%,var(--tobacco-pale) 100%);opacity:.85}
  .flavour-swirl-small{left:470px;top:520px;width:190px;height:70px;border-radius:40px;
    background:linear-gradient(90deg,var(--tobacco-pale),var(--tobacco));opacity:.85}
  .flavour-name{left:0;width:900px;top:318px;text-align:center;font-family:"Oswald",sans-serif;font-weight:500;font-size:80px;letter-spacing:2px}
  .flavour-rule{left:325px;top:425px;width:250px;height:4px;background:var(--ink)}
  .flavour-tagline{left:0;width:900px;top:444px;text-align:center;font-family:"Montserrat",sans-serif;font-weight:400;font-size:19px;letter-spacing:4px;color:#d8d8d8}
  .batch-info{left:14px;top:585px;transform:rotate(-90deg);transform-origin:left top;font-size:16px;white-space:nowrap}
  .producer{left:26px;top:640px;font-size:16px;line-height:18px;font-family:Arial,sans-serif}
  .producer .heading{font-size:18px;line-height:19px}
  .brand-name{left:0;width:900px;top:672px;text-align:center;font-size:56px;letter-spacing:3px;color:var(--brand)}
  .badge{left:710px;background:var(--badge);color:var(--badge-ink);text-align:center}
  .badge-collect{width:120px;height:38px;font-size:17px;line-height:17px;padding-top:2px}
  .badge-code{width:84px;height:34px;font-size:22px;line-height:34px}
  .badge-caption{left:710px;font-size:13px}
  .disposal-icons{left:700px;top:665px;width:150px;height:70px}
  .volume{left:718px;top:762px;font-size:21px;font-family:Arial,sans-serif}
</style>
</head>
<body>
<main class="label">
  <svg class="ring" viewBox="0 0 874 826" aria-hidden="true">
    <circle cx="450" cy="400" r="198" fill="none" stroke="var(--tobacco)" stroke-width="4"/>
  </svg>
  <div class="flavour-swirl" role="img" aria-label="Flowing tobacco-toned smoke waves"></div>
  <div class="flavour-swirl-small" role="img" aria-label="Small tobacco-toned smoke wave"></div>

  <p class="ingredients">INGREDIENTI:<br>GLICOLE<br>PROPILENICO<br>SOSTANZE<br>AROMATIZZANTI</p>

  <p class="instructions">ISTRUZIONI<br>D’USO:<br>Agitare bene prima dell’utilizzo. Diluire nelle percentuali consigliate sul nostro sito. Conservare in luogo fresco e asciutto</p>

  <h1 class="flavour-name">TOBACCO</h1>
  <div class="flavour-rule"></div>
  <p class="flavour-tagline">PREMIUM E-LIQUID</p>

  <p class="batch-info">L.SH20 - 001-PES-D.PROD 22-04-2022 D.SC 21-04-2024</p>

  <p class="producer"><span class="heading">PRODOTTO<br>E CONFEZIONATO<br>DA Nordvale srl</span><br>Via Lungo 18<br>10100 Torino<br>P.i.00000000000<br>Tel. +39 000 0000000<br>info@nordvale.it</p>

  <p class="brand-name">VAPORA LANE</p>

  <p class="badge badge-collect" style="top:408px">RACCOLTA<br>PLASTICA</p>
  <p class="badge-caption" style="top:452px">ETICHETTA</p>
  <p class="badge badge-code" style="top:470px">PAP 5</p>
  <p class="badge badge-collect" style="top:532px">RACCOLTA<br>PLASTICA</p>
  <p class="badge-caption" style="top:576px">FLACONE</p>
  <p class="badge badge-code" style="top:594px">PET 1</p>

  <svg class="disposal-icons" viewBox="0 0 150 70" aria-hidden="true">
    <g fill="none" stroke="var(--ink)" stroke-width="3">
      <path d="M30 10 L52 50 L8 50 Z"/>
      <path d="M98 25 h26 l-4 40 h-18 z"/>
      <path d="M95 25 h32"/>
    </g>
    <circle cx="132" cy="8" r="6" fill="var(--ink)"/>
    <rect x="128" y="16" width="8" height="26" fill="var(--ink)"/>
  </svg>

  <p class="volume">20 ML NET</p>
</main>
</body>
</html>
```